Supplement Company Needs a Protein Powder Pouch Design

We are looking for a modern and fresh design for our 500g pouches of protein powder as our current design is not eye catching or exciting enough.

This new design will be printed on both sides of a 178mm x 280mm x 101mm pouch.

We have 4 flavours. These are Banana Ice Cream, Chocolate Deluxe, Strawberries & Cream and Vanilla Ice Cream.

Industry/Entity Type

Supplement

Requirements
Must have
• Attractive and eye catching front and space for all the nutritional information and ingredients on the back.

Must clearly state 'food supplement' somewhere on the front of the pouch.
Nice to have
• Our logo is attached.
Should not have
• No health claims as these are not allowed in the UK

```html
<!DOCTYPE html>
<html lang="en">
<head>
<meta charset="utf-8">
<title>Stride Protein Powder Pouch – Chocolate Deluxe</title>
<link href="https://fonts.googleapis.com/css2?family=Josefin+Sans:wght@600;700&family=Arimo:wght@400;700&display=swap" rel="stylesheet">
<style>
  :root{
    --canvas:#ffffff;
    --cream:#f7d898;
    --cream-line:#e2bf7c;
    --band:#444446;
    --gold:#eac483;
    --gold-deep:#d9ad63;
    --ink:#2c2c2e;
    --body-on-band:#e6c48a;
    --cocoa:#5a3424;
    --cocoa-light:#8b5a3c;
  }
  *{box-sizing:border-box;margin:0;padding:0}
  html,body{width:1200px;height:1200px;overflow:hidden;background:var(--canvas)}
  body{font-family:"Arimo",Arial,sans-serif}

  .sheet{position:relative;width:1200px;height:1200px}
  .panel{position:absolute;top:310px;height:580px;background:var(--cream);overflow:hidden}
  .panel--front{left:55px;width:380px}
  .panel--back{left:485px;width:380px}
  .panel--gusset{left:915px;width:230px}

  .botanical{position:absolute;top:0;bottom:0;width:51px;
    background:linear-gradient(180deg,#f2cf8c 0%,#f0cb86 50%,#f2cf8c 100%)}
  .botanical--left{left:0}
  .botanical--right{right:0}
  .gusset-art{position:absolute;left:50%;transform:translateX(-50%);width:90px;
    background:radial-gradient(ellipse at center,#ebc27e 0%,#f3d190 70%,transparent 100%)}
  .gusset-art--top{top:20px;height:150px}
  .gusset-art--mid{top:175px;height:155px}
  .gusset-art--bottom{bottom:25px;height:110px}

  .band{position:absolute;top:0;bottom:0;left:51px;width:281px;background:var(--band);
    display:flex;flex-direction:column;align-items:center;padding:108px 18px 0}

  .brand-frame{position:relative;border:1px solid var(--gold);border-top:none;
    width:138px;height:42px;display:flex;align-items:flex-start;justify-content:center;padding-top:0}
  .brand-frame::before,.brand-frame::after{content:"";position:absolute;top:0;width:16px;height:1px;background:var(--gold)}
  .brand-frame::before{left:0}
  .brand-frame::after{right:0}
  .brand-name{font-family:"Josefin Sans",sans-serif;font-weight:700;font-size:22px;color:#ece6da;
    letter-spacing:1px;margin-top:-10px;display:flex;align-items:center;gap:5px}
  .brand-dot{width:6px;height:6px;border-radius:50%;background:var(--gold)}
  .food-label{position:absolute;bottom:-6px;left:50%;transform:translateX(-50%);background:var(--band);
    padding:0 6px;font-family:"Josefin Sans",sans-serif;font-weight:700;font-size:8px;color:var(--gold);
    letter-spacing:.6px;white-space:nowrap}

  .title{font-family:"Josefin Sans",sans-serif;font-weight:700;color:var(--gold);
    font-size:38px;line-height:40px;letter-spacing:2.5px;text-align:center;margin-top:14px}
  .flavour{background:var(--gold);color:var(--ink);font-family:"Arimo",sans-serif;font-size:11px;
    letter-spacing:.3px;padding:1px 5px;margin-top:1px;border:1px solid #222}

  .hero{width:148px;height:64px;margin-top:12px;border-radius:6px;
    background:radial-gradient(ellipse at 40% 55%,var(--cocoa-light) 0%,var(--cocoa) 55%,rgba(68,68,70,0) 80%)}

  .info{align-self:stretch;margin-top:8px;font-size:5.2px;line-height:6.4px;color:var(--body-on-band)}
  .info p{margin-bottom:3px}
  .tag{background:var(--gold);color:var(--ink);font-weight:700;padding:0 1px;margin-right:2px}
  .italic{font-style:italic}

  .nutrition{display:flex;gap:3px;margin:2px 0 6px}
  .nutrition table{flex:1;border-collapse:collapse;background:var(--gold-deep);color:#4a3a22}
  .nutrition td{border:.5px solid #6b5733;padding:0 2px;font-size:4.6px;line-height:6px}
  .servings{width:28px;background:var(--gold-deep);color:#3b2f1c;text-align:center;font-size:4.6px;line-height:5.5px;padding-top:3px}
  .servings b{display:block;font-size:11px;line-height:12px;font-family:"Josefin Sans",sans-serif}

  .footer-row{display:flex;justify-content:space-between;margin-top:4px}
  .weight{position:absolute;bottom:22px;left:50%;transform:translateX(-50%);background:var(--gold);
    color:var(--ink);font-size:6px;padding:1px 4px;border:1px solid #222}

  .gusset-copy{position:absolute;top:330px;left:0;right:0;text-align:center;font-size:6.3px;line-height:8px;color:#3a3226;padding:0 48px}
</style>
</head>
<body>
<main class="sheet">

  <!-- FRONT -->
  <section class="panel panel--front">
    <div class="botanical botanical--left" role="img" aria-label="Line-drawn cocoa pods and cocoa plant sprigs"></div>
    <div class="botanical botanical--right" role="img" aria-label="Line-drawn cocoa pods and cocoa plant sprigs"></div>
    <div class="band">
      <div class="brand-frame">
        <span class="brand-name"><span class="brand-dot"></span>STRIDE</span>
        <span class="food-label">FOOD SUPPLEMENT</span>
      </div>
      <h1 class="title">PROTEIN<br>POWDER</h1>
      <div class="flavour">CHOCOLATE DELUXE FLAVOUR</div>
      <div class="hero" role="img" aria-label="Milk chocolate pieces with a hazelnut and leaves"></div>
      <div class="info">
        <p><span class="tag">SUGGESTED USE:</span>We recommend using one to two servings of 30g per day. One serving is one level scoop. Mix one level scoop with at least 200ml of cold water. Do not exceed recommended daily dose.</p>
        <p><span class="tag">STORAGE INFORMATION:</span><br>Store in a cool and dry place. Reseal this pouch after each use. Keep out of sight and reach of children.</p>
        <div class="nutrition">
          <table>
            <tr><td>Typical Values</td><td>Per 30g</td><td>Per 100g</td><td>Typical Values</td><td>Per 30g</td><td>Per 100g</td></tr>
            <tr><td>Energy</td><td>486kJ</td><td>1620kJ</td><td>Fat</td><td>2.1g</td><td>7.0g</td></tr>
            <tr><td>of which saturates</td><td>0.9g</td><td>3.0g</td><td>Carbohydrate</td><td>3.6g</td><td>12g</td></tr>
            <tr><td>Protein</td><td>22g</td><td>73g</td><td>Salt</td><td>0.2g</td><td>0.7g</td></tr>
          </table>
          <div class="servings">Servings<br>per pack<b>117</b></div>
        </div>
        <p><span class="tag">INGREDIENTS:</span>Protein Blend (Soya Protein Isolate, Whey Protein Concentrate (Milk), Milk Protein) (79%), Acetyl Carnitine (500mg per 30g), Flavouring, Fat Reduced Cocoa Powder (10%), Thickener (Xanthan Gum), Sweetener (Sucralose).</p>
        <p class="italic">Manufactured in the UK with EU protein powder and non-EU cocoa powder.</p>
        <p><span class="tag">CAUTION:</span>Food supplements should not be used as a substitute for a varied diet and healthy lifestyle. This product is not recommended for use by pregnant or lactating women. If you are taking any medication or are under medical supervision, consult your health care professional before use. Not intended for use by persons under the age of 16.</p>
        <div class="footer-row"><span>Stride Nutrition Limited, 12 Mill Lane, Exeter, Devon, EX1 2AB.</span><span class="italic">Best before: See back of pouch</span></div>
      </div>
      <div class="weight">500g</div>
    </div>
  </section>

  <!-- BACK -->
  <section class="panel panel--back">
    <div class="botanical botanical--left" role="img" aria-label="Line-drawn cocoa pods and cocoa plant sprigs"></div>
    <div class="botanical botanical--right" role="img" aria-label="Line-drawn cocoa pods and cocoa plant sprigs"></div>
    <div class="band">
      <div class="brand-frame">
        <span class="brand-name"><span class="brand-dot"></span>STRIDE</span>
        <span class="food-label">FOOD SUPPLEMENT</span>
      </div>
      <h1 class="title">PROTEIN<br>POWDER</h1>
      <div class="flavour">CHOCOLATE DELUXE FLAVOUR</div>
      <div class="hero" role="img" aria-label="Milk chocolate pieces with a hazelnut and leaves"></div>
      <div class="info">
        <p><span class="tag">SUGGESTED USE:</span>We recommend using one to two servings of 30g per day. One serving is one level scoop. Mix one level scoop with at least 200ml of cold water. Do not exceed recommended daily dose.</p>
        <p><span class="tag">STORAGE INFORMATION:</span><br>Store in a cool and dry place. Reseal this pouch after each use. Keep out of sight and reach of children.</p>
        <div class="nutrition">
          <table>
            <tr><td>Typical Values</td><td>Per 30g</td><td>Per 100g</td><td>Typical Values</td><td>Per 30g</td><td>Per 100g</td></tr>
            <tr><td>Energy</td><td>486kJ</td><td>1620kJ</td><td>Fat</td><td>2.1g</td><td>7.0g</td></tr>
            <tr><td>of which saturates</td><td>0.9g</td><td>3.0g</td><td>Carbohydrate</td><td>3.6g</td><td>12g</td></tr>
            <tr><td>Protein</td><td>22g</td><td>73g</td><td>Salt</td><td>0.2g</td><td>0.7g</td></tr>
          </table>
          <div class="servings">Servings<br>per pack<b>117</b></div>
        </div>
        <p><span class="tag">INGREDIENTS:</span>Protein Blend (Soya Protein Isolate, Whey Protein Concentrate (Milk), Milk Protein) (79%), Acetyl Carnitine (500mg per 30g), Flavouring, Fat Reduced Cocoa Powder (10%), Thickener (Xanthan Gum), Sweetener (Sucralose).</p>
        <p class="italic">Manufactured in the UK with EU protein powder and non-EU cocoa powder.</p>
        <p><span class="tag">CAUTION:</span>Food supplements should not be used as a substitute for a varied diet and healthy lifestyle. This product is not recommended for use by pregnant or lactating women. If you are taking any medication or are under medical supervision, consult your health care professional before use. Not intended for use by persons under the age of 16.</p>
        <div class="footer-row"><span>Stride Nutrition Limited, 12 Mill Lane, Exeter, Devon, EX1 2AB.</span><span class="italic">Best before: 00-00-0000</span></div>
      </div>
      <div class="weight">500g</div>
    </div>
  </section>

  <!-- SIDE GUSSET -->
  <section class="panel panel--gusset">
    <div class="gusset-art gusset-art--top" role="img" aria-label="Line-drawn cocoa pod"></div>
    <div class="gusset-art gusset-art--mid" role="img" aria-label="Line-drawn cocoa plant sprig"></div>
    <p class="gusset-copy">Lorem ipsum dolor sit amet, consectetuer adipiscing elit, sed diam nonummy nibh euismod tincidunt ut laoreet dolore magna aliquam erat volutpat. Ut wisi enim ad minim veniam, quis nostrud exerci tation ullamcorper suscipit lobortis nisl ut aliquip ex ea commodo consequat. Duis autem vel eum iriure dolor in hendrerit in vulputate velit esse molestie consequat, vel illum dolore eu feugiat nulla facilisis at vero eros et</p>
    <div class="gusset-art gusset-art--bottom" role="img" aria-label="Line-drawn cocoa pod"></div>
  </section>

</main>
</body>
</html>
```